Voltarra: Electrical Contractor flyer design.

We are looking for a sharp and professional flyer to promote the business's cost for specific jobs and to promote the business.
We are a small electrical business looking to break into the market.
Attached logo to be used and following content to be incorporated. Contact details will be given upon final flyer design.

Internal Power Points: $ 120
External Weather Proof Power Points: $150
T.V. Points: $120 (excludes aerial)
T.V. Mounting: $ 200 (Exclude Leads)
Aerials Starting From: $220 Incudes Mast
LED Down lights: $60 per unti
Ceiling Fans: $150 (Fan Excluded)
Oven & Range Hood Change Overs: $250
A.C. Install: $300
S/B Upgrade: From $600
Safety Switch Installation: $280
Phone Points: $120

Services Incude:

New home wiring
Shop & Office Fit Outs
Re - Wires
Extentions
Garden Lighting
Home Thearters
Home Automation
Power Points
Phone, Data
Feature Lighting
Lighting design and Installation
Ceiling Fans
A.C Installation
Oven & Range hood Installation

*All prices are gst inclusive
**Prices subject to change due to site access.

```html
<!DOCTYPE html>
<html lang="en">
<head>
<meta charset="utf-8">
<title>Voltarra – Electrical Services Flyer</title>
<link rel="stylesheet" href="https://fonts.googleapis.com/css2?family=Roboto:ital,wght@0,400;0,500;0,700;0,900;1,400;1,700&family=Russo+One&display=swap">
<style>
  :root {
    --orange: #ef6b25;
    --orange-deep: #e2631a;
    --text-grey: #474747;
    --heading-grey: #555555;
    --price-ink: #333333;
    --rule: #444444;
    --white: #ffffff;
  }
  * { margin: 0; padding: 0; box-sizing: border-box; }
  html, body { width: 846px; height: 1200px; overflow: hidden; background: var(--white); }
  .flyer {
    position: relative;
    width: 846px;
    height: 1200px;
    overflow: hidden;
    background: var(--white);
    font-family: "Roboto", Arial, sans-serif;
  }
  .hero {
    position: absolute; left: 0; top: 0;
    width: 846px; height: 448px;
    background: radial-gradient(ellipse 60% 75% at 50% 30%, #fde9dc 0%, #f9b790 40%, var(--orange) 85%);
  }
  .hero-photo {
    position: absolute; left: 280px; top: 0;
    width: 248px; height: 412px;
    background: linear-gradient(90deg, rgba(110,160,220,.55) 0%, rgba(110,160,220,.55) 33%, rgba(240,120,40,.55) 33%, rgba(240,120,40,.55) 66%, rgba(220,220,60,.55) 66%);
    border-radius: 6px 6px 0 0;
  }
  .price-list {
    position: absolute; top: 26px;
    width: 236px; height: 372px;
    display: flex; flex-direction: column; justify-content: space-between;
    list-style: none;
    color: var(--price-ink);
  }
  .price-list--left { left: 26px; }
  .price-list--right { left: 572px; }
  .price-item { display: flex; flex-direction: column; }
  .price-item__job { font-size: 14px; font-weight: 700; line-height: 17px; }
  .price-item__cost { font-size: 22px; font-weight: 900; line-height: 26px; color: var(--white); text-shadow: 0 1px 2px rgba(0,0,0,.35); }
  .price-item__note { font-size: 12px; font-weight: 500; font-style: italic; text-shadow: none; color: var(--price-ink); margin-left: 4px; }
  .tab {
    position: absolute; left: 170px; top: 412px;
    width: 514px; height: 60px;
    background: var(--white);
    border-radius: 18px 18px 0 0;
  }
  .section-title {
    position: absolute; left: 0; width: 846px;
    text-align: center;
    font-family: "Russo One", sans-serif;
    font-style: italic;
    color: var(--heading-grey);
    letter-spacing: 1px;
    text-transform: uppercase;
  }
  .services-title { top: 432px; font-size: 27px; transform: skewX(-8deg); }
  .services {
    position: absolute; top: 502px; left: 64px;
    display: grid;
    grid-template-columns: 329px 400px;
    row-gap: 8.3px;
    list-style: none;
  }
  .services li {
    display: flex; align-items: center;
    height: 24px;
    font-size: 22px; font-weight: 500;
    color: var(--text-grey);
    white-space: nowrap;
  }
  .services li::before {
    content: ""; width: 17px; height: 17px;
    background: var(--orange-deep);
    margin-right: 8px; flex: none;
  }
  .notes {
    position: absolute; left: 72px; top: 759px;
    width: 701px; height: 77px;
    border-top: 1.5px solid var(--rule);
    border-bottom: 1.5px solid var(--rule);
    text-align: center;
    font-style: italic; font-size: 19px;
    color: var(--text-grey);
    line-height: 32px;
    padding-top: 5px;
  }
  .contact-title { top: 858px; font-size: 19px; transform: skewX(-8deg); }
  .contact {
    position: absolute; left: 0; top: 895px; width: 846px;
    text-align: center;
    font-style: italic; font-weight: 700; font-size: 22px;
    color: var(--orange-deep);
    line-height: 28.5px;
  }
  .footer-band { position: absolute; left: 0; top: 1019px; width: 846px; height: 181px; }
  .brand {
    position: absolute; left: 0; top: 1070px; width: 846px;
    display: flex; flex-direction: column; align-items: center;
  }
  .brand-name {
    display: flex; align-items: center; gap: 12px;
    font-size: 46px; font-weight: 700;
    color: var(--text-grey);
    line-height: 1;
  }
  .brand-name::before {
    content: ""; width: 26px; height: 26px; background: var(--orange-deep);
  }
  .brand-suffix {
    margin-top: 4px; margin-left: 200px;
    font-size: 9px; color: var(--text-grey);
  }
</style>
</head>
<body>
<div class="flyer">
  <header class="hero">
    <div class="hero-photo" role="img" aria-label="Photo of three stripped electrical wires – blue, orange and yellow-green – with exposed copper strands"></div>

    <ul class="price-list price-list--left">
      <li class="price-item"><span class="price-item__job">Internal Power Points</span><span class="price-item__cost">$120</span></li>
      <li class="price-item"><span class="price-item__job">External Weather Proof Power Points</span><span class="price-item__cost">$150</span></li>
      <li class="price-item"><span class="price-item__job">T.V. Points</span><span class="price-item__cost">$120<span class="price-item__note">(excludes aerial)</span></span></li>
      <li class="price-item"><span class="price-item__job">T.V. Mounting</span><span class="price-item__cost">$200<span class="price-item__note">(Exclude Leads)</span></span></li>
      <li class="price-item"><span class="price-item__job">Aerials Starting From</span><span class="price-item__cost">$220<span class="price-item__note">Incudes Mast</span></span></li>
      <li class="price-item"><span class="price-item__job">LED Down lights</span><span class="price-item__cost">$60<span class="price-item__note">per unti</span></span></li>
    </ul>

    <ul class="price-list price-list--right">
      <li class="price-item"><span class="price-item__job">Ceiling Fans</span><span class="price-item__cost">$150<span class="price-item__note">(Fan Excluded)</span></span></li>
      <li class="price-item"><span class="price-item__job">Oven &amp; Range Hood Change Overs</span><span class="price-item__cost">$250</span></li>
      <li class="price-item"><span class="price-item__job">A.C. Install</span><span class="price-item__cost">$300</span></li>
      <li class="price-item"><span class="price-item__job">S/B Upgrade</span><span class="price-item__cost"><span class="price-item__note" style="margin:0 4px 0 0">From</span>$600</span></li>
      <li class="price-item"><span class="price-item__job">Safety Switch Installation</span><span class="price-item__cost">$280</span></li>
      <li class="price-item"><span class="price-item__job">Phone Points</span><span class="price-item__cost">$120</span></li>
    </ul>
  </header>
  <div class="tab"></div>

  <h2 class="section-title services-title">Services Include:</h2>
  <ul class="services">
    <li>New home wiring</li><li>Power Points</li>
    <li>Shop &amp; Office Fit Outs</li><li>Phone, Data</li>
    <li>Re - Wires</li><li>Feature Lighting</li>
    <li>Extentions</li><li>Lighting design and Installation</li>
    <li>Garden Lighting</li><li>Ceiling Fans</li>
    <li>Home Thearters</li><li>A.C Installation</li>
    <li>Home Automation</li><li>Oven &amp; Range hood Installation</li>
  </ul>

  <div class="notes">
    <p>*All prices are gst inclusive</p>
    <p>**Prices subject to change due to site access</p>
  </div>

  <h2 class="section-title contact-title">Contact Us</h2>
  <div class="contact">
    <p>office@voltarra.com</p>
    <p>+1 555 01 234 56</p>
    <p>www.voltarra.com | social page</p>
  </div>

  <svg class="footer-band" viewBox="0 0 846 181" aria-hidden="true">
    <defs>
      <linearGradient id="bandFill" x1="0" y1="0" x2="1" y2="0">
        <stop offset="0" stop-color="#e8662a"/>
        <stop offset="1" stop-color="#f07325"/>
      </linearGradient>
    </defs>
    <rect width="846" height="181" fill="url(#bandFill)"/>
    <polygon points="174,0 686,0 646,181 128,181" fill="#ffffff"/>
  </svg>

  <div class="brand">
    <div class="brand-name">Voltarra</div>
    <div class="brand-suffix">pty ltd</div>
  </div>
</div>
</body>
</html>
```